Classy, Elegant, Simple Business Card Design

Looking to have a classy, simple, and elegant design. Want a top notch designed business card. I really like the look of the new brivo credit card. I also like the design I attached. I am trying to reach 21-29 year old females for booking us for there wedding or event. We offer Disc Jockey Service, Photo Booth Rentals, and Uplighting .

Target Market(s)

21-28 year old females

Contact Information for Business Card

Has to have logo, website, email, and phone number

Font styles to use
Other font styles liked:
• open to font choice, modern, clean
Designer to choose
33a6d7
0791cd
0555a3
ffffff

Requirements
Must have
• Has to have logo, website, email, and phone number
Nice to have
• I really like the design of the new brivo credit card. I also included my logo and some designs I like
Should not have
• clutter or too much info

```html
<!DOCTYPE html>
<html lang="en">
<head>
<meta charset="utf-8">
<title>Tidelight Event Group – Business Card</title>
<link href="https://fonts.googleapis.com/css2?family=Jost:wght@400;500;600&display=swap" rel="stylesheet">
<style>
  :root {
    --backdrop: #e9ebee;
    --card: #ffffff;
    --brand-blue: #0555a3;
    --brand-mid: #0791cd;
    --brand-light: #33a6d7;
    --ink: #1f2a44;
    --muted: #4a4f5a;
  }
  * { box-sizing: border-box; margin: 0; padding: 0; }
  html, body {
    width: 1200px;
    height: 800px;
    overflow: hidden;
    background: var(--backdrop);
    font-family: "Jost", "Helvetica Neue", Arial, sans-serif;
  }
  .canvas {
    position: relative;
    width: 1200px;
    height: 800px;
    display: flex;
    align-items: center;
    justify-content: center;
    gap: 60px;
  }
  .card {
    position: relative;
    width: 490px;
    height: 280px;
    background: var(--card);
    border-radius: 4px;
    box-shadow: 0 10px 28px rgba(20, 30, 50, 0.12);
  }

  /* Front */
  .card--front {
    display: flex;
    flex-direction: column;
    align-items: center;
    justify-content: center;
    gap: 14px;
  }
  .brand {
    display: flex;
    align-items: center;
    gap: 10px;
  }
  .brand__dot {
    width: 18px;
    height: 18px;
    border-radius: 50%;
    background: var(--brand-blue);
  }
  .brand__name {
    color: var(--brand-blue);
    font-weight: 500;
    font-size: 26px;
    letter-spacing: 0.06em;
    text-transform: uppercase;
  }
  .card--front .website {
    color: var(--brand-blue);
    font-size: 17px;
    letter-spacing: 0.02em;
  }

  /* Back */
  .contact {
    position: absolute;
    top: 30px;
    left: 32px;
    color: var(--muted);
    font-size: 14px;
    line-height: 1.6;
    letter-spacing: 0.02em;
  }
  .identity {
    position: absolute;
    right: 34px;
    bottom: 34px;
    text-align: right;
  }
  .identity .brand {
    justify-content: flex-end;
    margin-bottom: 10px;
  }
  .identity .brand__dot { width: 12px; height: 12px; }
  .identity .brand__name { font-size: 16px; }
  .person__name {
    color: var(--ink);
    font-weight: 600;
    font-size: 20px;
    letter-spacing: 0.08em;
    text-transform: uppercase;
  }
  .person__title {
    color: var(--brand-blue);
    font-size: 14px;
    margin-top: 2px;
  }
</style>
</head>
<body>
  <main class="canvas">
    <section class="card card--front" aria-label="Card front">
      <div class="brand">
        <span class="brand__dot" aria-hidden="true"></span>
        <span class="brand__name">Tidelight Event Group</span>
      </div>
      <p class="website">tidelighteventgroup.com</p>
    </section>

    <section class="card card--back" aria-label="Card back">
      <div class="contact">
        <p class="contact__phone">555-014-2290</p>
        <p class="contact__email">info@TidelightEventGroup.com</p>
      </div>
      <div class="identity">
        <div class="brand">
          <span class="brand__dot" aria-hidden="true"></span>
          <span class="brand__name">Tidelight Event Group</span>
        </div>
        <p class="person__name">Dana Whitlow</p>
        <p class="person__title">Manager</p>
      </div>
    </section>
  </main>
</body>
</html>
```